Teach English in China Website Redesign Needed

We recruit native English speakers from the US, UK, etc. who want to teach English as a foreign language in schools in China. Our target customer is college educated, age 22-28 and they love to travel. We prefer designs with bright colors and lots of photos. We want to keep all the text on our current homepage, LanternClassroomHub.com. We are open to changing our logo. A competitor's page that we like is bluepeakmentors.com because of their bright colors, photos and use of white space. We are happy to give you a dofollow link and design credit on our homepage. The use of included photos is optional. We need at least a home page design and a standard blog post design.
Target Market(s)
Our target customer is college educated, age 22-28 and they love to travel. Half of our customers are kindergarten teachers. Half of our customers are male.
Logo Text
Lantern Classroom Hub
Number of Pages Required
2 page
Requirements
Must have
- Bright colors
Should not have
- Our homepage must not look crowded. Use white space effectively.

```html
<!DOCTYPE html>
<html lang="en">
<head>
<meta charset="utf-8">
<title>Lantern Classroom Hub – Teach English in China</title>
<link href="https://fonts.googleapis.com/css2?family=Open+Sans:wght@300;400;600;700&display=swap" rel="stylesheet">
<style>
:root{
  --ink:#111;
  --black:#0b0b0b;
  --text:#333;
  --muted:#9a9a9a;
  --accent:#e8675c;
  --accent-dark:#c9524a;
  --line:#e4e4e4;
  --pale:#f3f3f3;
  --white:#fff;
}
*{box-sizing:border-box;margin:0;padding:0}
html,body{width:1200px;height:3213px;overflow:hidden}
body{font-family:"Open Sans",Arial,sans-serif;color:var(--text);background:var(--white);position:relative}
.abs{position:absolute}

/* top bar */
.topbar{position:absolute;left:0;top:0;width:1200px;height:33px;background:var(--black)}
.topbar nav{position:absolute;left:40px;top:0;height:33px;display:flex;gap:26px;align-items:center}
.topbar a{color:var(--white);font-size:12px;font-weight:600;text-decoration:none;letter-spacing:.3px}
.social{position:absolute;display:flex;gap:5px}
.social span{width:14px;height:14px;border-radius:50%;background:#777;display:block}
.topbar .social{right:82px;top:9px}

/* header */
.header{position:absolute;left:0;top:33px;width:1200px;height:123px;background:var(--white)}
.brand{position:absolute;left:44px;top:38px;font-size:26px;font-weight:700;color:var(--ink);letter-spacing:.2px}
.mainnav{position:absolute;left:575px;top:49px;display:flex;gap:19px}
.mainnav a{font-size:16px;font-weight:600;color:var(--ink);text-decoration:none}
.mainnav a.active{border-bottom:2px solid var(--ink);padding-bottom:2px}
.search{position:absolute;left:1128px;top:44px}

/* hero */
.hero{position:absolute;left:0;top:156px;width:1200px;height:555px;
  background:linear-gradient(180deg,#c8d3dc 0%,#d9c7b0 38%,#e9a56f 55%,#6f7a86 72%,#4d5a66 100%)}
.hero::after{content:"";position:absolute;right:0;top:0;width:520px;height:555px;
  background:radial-gradient(circle at 85% 52%,rgba(255,220,150,.95) 0,rgba(255,170,90,.55) 18%,rgba(255,150,80,0) 55%)}
.hero-copy{position:absolute;left:40px;top:296px;color:var(--white);z-index:2}
.hero-copy .lead{font-size:30px;font-weight:400}
.hero-copy h1{font-size:46px;font-weight:600;margin-top:8px;letter-spacing:.5px}
.hero .arrow{position:absolute;top:258px;z-index:2}

/* section titles */
.section-title{position:absolute;left:0;width:1200px;text-align:center;font-size:37px;font-weight:400;color:var(--ink);letter-spacing:.5px}
.section-sub{position:absolute;left:320px;width:560px;text-align:center;font-size:12px;line-height:19px;color:var(--muted)}

/* featured */
.photo{display:block}
.body-copy{font-size:12px;line-height:15px;color:#b0b0b0;letter-spacing:.4px}
.body-copy p+p{margin-top:14px}
.meta{font-size:11px;color:var(--accent)}
.meta b{font-weight:400;color:var(--text)}
.btn{display:flex;align-items:center;justify-content:center;background:var(--accent);color:var(--white);
  font-size:10px;font-weight:700;text-transform:uppercase;letter-spacing:.5px}
.btn-more{position:absolute;left:549px;top:1182px;width:93px;height:29px}
.btn-more::after{content:"";position:absolute;left:38px;bottom:-8px;border:8px solid transparent;border-top-color:var(--accent);border-bottom:0}
.divider{position:absolute;left:0;top:1233px;width:1200px;height:2px;background:var(--line)}

/* grid */
.grid{position:absolute;left:113px;top:1291px;display:grid;grid-template-columns:repeat(4,225px);column-gap:21px;row-gap:0}
.card{height:289px}
.card:nth-child(n+9){height:300px}
.card .photo{height:127px}
.card h3{font-size:12px;font-weight:700;color:var(--ink);margin-top:26px}
.card p{font-size:8.5px;line-height:13px;color:#999;margin-top:9px}
.card .meta{font-size:8px;margin-top:9px;display:block;padding-bottom:9px;border-bottom:1px solid #eee}
.p-girl{background:linear-gradient(135deg,#b4432c 0%,#d8936a 45%,#e8d9c8 75%,#b93a2a 100%)}
.p-kids{background:linear-gradient(135deg,#7a7e55 0%,#f3f2ef 35%,#3b8a5c 60%,#e8e6e0 100%)}
.p-class{background:linear-gradient(135deg,#2a2f2c 0%,#3a6c4a 35%,#c2402f 55%,#2d3350 100%)}
.circle-arrow{position:absolute;width:44px;height:58px;border-radius:22px;background:#cfcfcf}

/* blog of the day */
.day{position:absolute;left:0;top:2195px;width:1200px;height:465px;
  background:linear-gradient(180deg,#f7f7f7 0%,#ededed 60%,#e2e2e2 100%)}
.day .photo{position:absolute;left:67px;top:116px;width:340px;height:211px;
  background:linear-gradient(180deg,#9fb8c6 0%,#b7c5b0 45%,#5d7a55 75%,#6d8a8f 100%)}
.day .body-copy{position:absolute;left:431px;top:117px;width:610px;color:#c4c4c4}
.day .meta{position:absolute;left:72px;top:344px}
.day .meta{color:#e0a800}

/* subscribe */
.subscribe{position:absolute;left:0;top:2660px;width:1200px;height:91px;background:var(--white)}
.field{position:absolute;top:27px;height:35px;background:#e9e9e9;color:#bbb;font-size:22px;padding-left:10px;line-height:35px}
.btn-sub{position:absolute;left:842px;top:31px;width:94px;height:27px}

/* apply band */
.apply{position:absolute;left:0;top:2751px;width:1200px;height:195px;
  background:linear-gradient(90deg,#6f8db8 0%,#b9c3cf 18%,#d3d5d7 45%,#c6c8ca 80%,#d8b79c 92%,#3a5e8a 100%)}
.btn-apply{position:absolute;left:518px;top:73px;width:160px;height:47px;font-size:13px;box-shadow:0 2px 0 var(--accent-dark)}

/* footer */
.footer{position:absolute;left:0;top:2946px;width:1200px;height:267px;background:var(--black);color:var(--white)}
.footer h4{font-size:11px;font-weight:700;letter-spacing:1px;text-transform:uppercase}
.footer .col{position:absolute;top:52px}
.footer .col p,.footer .col li{font-size:10px;line-height:15px;color:#ddd;list-style:none}
.footer .col h4+*{margin-top:16px}
.footer .brand-foot{position:absolute;left:880px;top:82px;font-size:22px;font-weight:700;color:#cfcfcf}
.contact-row{display:flex;gap:10px;align-items:flex-start;margin-bottom:10px}
.footer .bottom{position:absolute;left:0;bottom:0;width:1200px;height:35px;background:#1a1a1a}
.footer .bottom small{position:absolute;left:144px;top:11px;font-size:10px;color:#777}
.footer .social{right:82px;top:11px}
</style>
</head>
<body>

<header class="topbar">
  <nav>
    <a>JOB BOARD</a><a>APPLY</a><a>BLOG</a><a>HIRE A TEACHER</a><a>ABOUT US</a>
  </nav>
  <div class="social" aria-hidden="true"><span></span><span></span><span></span><span></span><span></span><span></span><span></span></div>
</header>

<div class="header">
  <div class="brand">Lantern Classroom Hub</div>
  <nav class="mainnav">
    <a class="active">Home</a><a>Available Jobs</a><a>Apply Online</a><a>Blog</a><a>About</a><a>FAQ</a>
  </nav>
  <svg class="search" width="32" height="32" viewBox="0 0 32 32" aria-label="Search">
    <circle cx="13" cy="13" r="9" fill="none" stroke="#9a9a9a" stroke-width="4"/>
    <line x1="20" y1="20" x2="29" y2="29" stroke="#9a9a9a" stroke-width="5" stroke-linecap="round"/>
  </svg>
</div>

<section class="hero" role="img" aria-label="Shanghai skyline along the river at sunset">
  <svg class="arrow" style="left:18px" width="22" height="40" viewBox="0 0 22 40"><polyline points="18,3 4,20 18,37" fill="none" stroke="#fff" stroke-width="3"/></svg>
  <svg class="arrow" style="right:18px" width="22" height="40" viewBox="0 0 22 40"><polyline points="4,3 18,20 4,37" fill="none" stroke="#fff" stroke-width="3"/></svg>
  <div class="hero-copy">
    <div class="lead">We will help you</div>
    <h1>TEACH ENGLISH IN CHINA</h1>
  </div>
</section>

<h2 class="section-title" style="top:750px">OUR BLOG</h2>
<p class="section-sub" style="top:812px">Lorem ipsum dolor sit amet, consectetur adipiscing elit. Nam odio magna, interdum vel neque nec, tempor sollicitudin lorem. Quisque at tincidunt odio.</p>

<div class="abs photo p-girl" style="left:67px;top:884px;width:422px;height:278px" role="img" aria-label="Young girl eating noodles with chopsticks"></div>
<div class="abs body-copy" style="left:518px;top:890px;width:610px">
  <p>Lorem ipsum dolor sit amet, consectetur adipiscing elit. Quisque elementum, nisl at condimentum sagittis, est felis elementum leo, vitae accumsan velit mauris sit amet odio. Maecenas id diam in velit pellentesque egestas. Integer vestibulum, est vel scelerisque viverra, purus ligula tincidunt enim, a tristique nulla lectus ac sapien. Aliquam cursus ipsum vestibulum sapien tempor luctus. Orci varius natoque penatibus et magnis dis parturient montes, nascetur ridiculus mus.</p>
  <p>Nunc laoreet rhoncus metus, at pretium ante elementum ac. Etiam consectetur enim sed, at bibendum enim ultrices quis. Sed ornare, metus vel dapibus sollicitudin, mi elit ornare sem, et vulputate ante elit id diam.</p>
  <p>In scelerisque felis eget velit posuere gravida. Sed at eleifend purus, eu finibus velit. Fusce mollis vel diam at dignissim. Pellentesque habitant morbi tristique senectus et netus et malesuada fames ac turpis egestas. Ut at nisl consectetur, tempor massa ac, facilisis metus. Nullam tristique massa at ante facilisis, vitae convallis arcu luctus. Morbi finibus convallis porttitor. Duis elementum quis risus vestibulum tincidunt. Vestibulum eleifend purus non nunc mollis pulvinar. Quisque hendrerit dui vel egestas consectetur.</p>
</div>
<div class="abs meta" style="left:72px;top:1182px">09.Sep2015<b>/By </b>Editor<b>/</b>1 Comments</div>
<div class="btn btn-more">View more</div>
<div class="divider"></div>

<div class="circle-arrow" style="left:31px;top:1682px"><svg width="44" height="58" viewBox="0 0 44 58"><polyline points="26,18 16,29 26,40" fill="none" stroke="#fff" stroke-width="3"/></svg></div>
<div class="circle-arrow" style="left:1116px;top:1682px"><svg width="44" height="58" viewBox="0 0 44 58"><polyline points="18,18 28,29 18,40" fill="none" stroke="#fff" stroke-width="3"/></svg></div>

<div class="grid">
  <article class="card"><div class="photo p-girl" role="img" aria-label="Girl eating noodles"></div><h3>Lorem ipsum dolor sit amet</h3><p>Lorem ipsum dolor sit amet, consectetur adipiscing elit, sed do eiusmod tempor incididunt ut labore et dolore magna aliqua. Ut enim ad minim veniam, quis</p><span class="meta">09.Sep2015<b>/By </b>Editor<b>/</b>1 Comments</span></article>
  <article class="card"><div class="photo p-kids" role="img" aria-label="Pupils in school uniforms lined up"></div><h3>Lorem ipsum dolor sit amet</h3><p>Lorem ipsum dolor sit amet, consectetur adipiscing elit, sed do eiusmod tempor incididunt ut labore et dolore magna aliqua. Ut enim ad minim veniam, quis</p><span class="meta">10.Sep2015<b>/By </b>Editor<b>/</b>1 Comments</span></article>
  <article class="card"><div class="photo p-class" role="img" aria-label="Teacher with children in a classroom"></div><h3>Lorem ipsum dolor sit amet</h3><p>Lorem ipsum dolor sit amet, consectetur adipiscing elit, sed do eiusmod tempor incididunt ut labore et dolore magna aliqua. Ut enim ad minim veniam, quis</p><span class="meta">10.Sep2015<b>/By </b>Editor<b>/</b>1 Comments</span></article>
  <article class="card"><div class="photo p-girl" role="img" aria-label="Girl eating noodles"></div><h3>Lorem ipsum dolor sit amet</h3><p>Lorem ipsum dolor sit amet, consectetur adipiscing elit, sed do eiusmod tempor incididunt ut labore et dolore magna aliqua. Ut enim ad minim veniam, quis</p><span class="meta">09.Sep2015<b>/By </b>Editor<b>/</b>1 Comments</span></article>

  <article class="card"><div class="photo p-girl" role="img" aria-label="Girl eating noodles"></div><h3>Lorem ipsum dolor sit amet</h3><p>Lorem ipsum dolor sit amet, consectetur adipiscing elit, sed do eiusmod tempor incididunt ut labore et dolore magna aliqua. Ut enim ad minim veniam, quis</p><span class="meta">09.Sep2015<b>/By </b>Editor<b>/</b>1 Comments</span></article>
  <article class="card"><div class="photo p-kids" role="img" aria-label="Pupils in school uniforms lined up"></div><h3>Lorem ipsum dolor sit amet</h3><p>Lorem ipsum dolor sit amet, consectetur adipiscing elit, sed do eiusmod tempor incididunt ut labore et dolore magna aliqua. Ut enim ad minim veniam, quis</p><span class="meta">10.Sep2015<b>/By </b>Editor<b>/</b>1 Comments</span></article>
  <article class="card"><div class="photo p-class" role="img" aria-label="Teacher with children in a classroom"></div><h3>Lorem ipsum dolor sit amet</h3><p>Lorem ipsum dolor sit amet, consectetur adipiscing elit, sed do eiusmod tempor incididunt ut labore et dolore magna aliqua. Ut enim ad minim veniam, quis</p><span class="meta">10.Sep2015<b>/By </b>Editor<b>/</b>1 Comments</span></article>
  <article class="card"><div class="photo p-girl" role="img" aria-label="Girl eating noodles"></div><h3>Lorem ipsum dolor sit amet</h3><p>Lorem ipsum dolor sit amet, consectetur adipiscing elit, sed do eiusmod tempor incididunt ut labore et dolore magna aliqua. Ut enim ad minim veniam, quis</p><span class="meta">09.Sep2015<b>/By </b>Editor<b>/</b>1 Comments</span></article>

  <article class="card"><div class="photo p-girl" role="img" aria-label="Girl eating noodles"></div><h3>Lorem ipsum dolor sit amet</h3><p>Lorem ipsum dolor sit amet, consectetur adipiscing elit, sed do eiusmod tempor incididunt ut labore et dolore magna aliqua. Ut enim ad minim veniam, quis</p><span class="meta">09.Sep2015<b>/By </b>Editor<b>/</b>1 Comments</span></article>
  <article class="card"><div class="photo p-kids" role="img" aria-label="Pupils in school uniforms lined up"></div><h3>Lorem ipsum dolor sit amet</h3><p>Lorem ipsum dolor sit amet, consectetur adipiscing elit, sed do eiusmod tempor incididunt ut labore et dolore magna aliqua. Ut enim ad minim veniam, quis</p><span class="meta">10.Sep2015<b>/By </b>Editor<b>/</b>1 Comments</span></article>
  <article class="card"><div class="photo p-class" role="img" aria-label="Teacher with children in a classroom"></div><h3>Lorem ipsum dolor sit amet</h3><p>Lorem ipsum dolor sit amet, consectetur adipiscing elit, sed do eiusmod tempor incididunt ut labore et dolore magna aliqua. Ut enim ad minim veniam, quis</p><span class="meta">10.Sep2015<b>/By </b>Editor<b>/</b>1 Comments</span></article>
  <article class="card"><div class="photo p-girl" role="img" aria-label="Girl eating noodles"></div><h3>Lorem ipsum dolor sit amet</h3><p>Lorem ipsum dolor sit amet, consectetur adipiscing elit, sed do eiusmod tempor incididunt ut labore et dolore magna aliqua. Ut enim ad minim veniam, quis</p><span class="meta">09.Sep2015<b>/By </b>Editor<b>/</b>1 Comments</span></article>
</div>

<section class="day" aria-label="Blog of the day">
  <h2 class="section-title" style="top:36px">BLOG OF THE DAY</h2>
  <div class="photo" role="img" aria-label="Fisherman on a bamboo raft on the Li River"></div>
  <div class="body-copy">
    <p>Lorem ipsum dolor sit amet, consectetur adipiscing elit. Quisque elementum, nisl at condimentum sagittis, est felis elementum leo, vitae accumsan velit mauris sit amet odio. Maecenas id diam in velit pellentesque egestas. Integer vestibulum, est vel scelerisque viverra, purus ligula tincidunt enim, a tristique nulla lectus ac sapien. Aliquam cursus ipsum vestibulum sapien tempor luctus. Orci varius natoque penatibus et magnis dis parturient montes, nascetur ridiculus mus.</p>
    <p>Nunc laoreet rhoncus metus, at pretium ante elementum ac. Etiam consectetur enim sed, at bibendum enim ultrices quis. Sed ornare, metus vel dapibus sollicitudin, mi elit ornare sem, et vulputate ante elit id diam.</p>
    <p>In scelerisque felis eget velit posuere gravida. Sed at eleifend purus, eu finibus velit. Fusce mollis vel diam at dignissim. Pellentesque habitant morbi tristique senectus et netus et malesuada fames ac turpis egestas. Ut at nisl consectetur, tempor massa ac, facilisis metus.</p>
  </div>
  <div class="meta">09.Sep2015<b>/By </b>Editor<b>/</b>1 Comments</div>
</section>

<section class="subscribe" aria-label="Newsletter">
  <div class="field" style="left:269px;width:264px">Name</div>
  <div class="field" style="left:551px;width:265px">Email</div>
  <div class="btn btn-sub">View more</div>
</section>

<section class="apply" role="img" aria-label="City skyline with modern tower and smiling young teacher">
  <div class="btn btn-apply">Apply now</div>
</section>

<footer class="footer">
  <div class="col" style="left:144px;width:180px">
    <h4>Our Mission</h4>
    <p>Lorem Ipsum is simply dummy text of the printing and typesetting industry. Lorem Ipsum has been the industry's standard dummy text ever since the 1500s, when an unknown printer took a galley of type and scrambled it to make.</p>
  </div>
  <div class="col" style="left:378px">
    <h4>Quick Links</h4>
    <ul><li>Company</li><li>Services</li><li>Solutions</li><li>Resources</li><li>Career</li><li>Contact Us</li></ul>
  </div>
  <div class="col" style="left:613px">
    <h4>Contact</h4>
    <div>
      <div class="contact-row">
        <svg width="9" height="12" viewBox="0 0 9 12"><path d="M4.5 0A4.5 4.5 0 0 0 0 4.5C0 8 4.5 12 4.5 12S9 8 9 4.5A4.5 4.5 0 0 0 4.5 0Z" fill="#fff"/><circle cx="4.5" cy="4.5" r="1.6" fill="#0b0b0b"/></svg>
        <p>2480 Harbor Lane,<br>Suite 210<br>Riverton, CO 80000</p>
      </div>
      <div class="contact-row">
        <svg width="9" height="12" viewBox="0 0 9 12"><rect x="1" y="0" width="7" height="12" rx="1.5" fill="#fff"/><rect x="2.3" y="1.5" width="4.4" height="7" fill="#0b0b0b"/></svg>
        <p>+61 9 5550 0142<br><br>0402 555 018</p>
      </div>
    </div>
  </div>
  <div class="brand-foot">Lantern Classroom Hub</div>
  <div class="bottom">
    <small>© 2015 lanternclassroomhub.com All rights reserved</small>
    <div class="social" aria-hidden="true"><span></span><span></span><span></span></div>
  </div>
</footer>

</body>
</html>
```